I need book cover graphics for 2/4 short pdf monographs
Titles:
1. Can Gardeners Really Outlast Winter Frost?
Hard Lessons Regarding Soil and Seasons
2. 7 Tricks every Orchard Keeper Quietly Hides
I want to use the same/similar cover design a second time for Plastic (Cosmetic) Surgery so the covers should be generic medical, perhaps with some images reference to beauty in the case or Plastic Surgery and weight loss in the case of Bariatric Surgery. You would just change the title block to refer to the other specialty, substituting Cosmetic for Weight Loss and Plastic for Bariatric.
Size is 6"x9" or A5

```html
<!DOCTYPE html>
<html lang="en">
<head>
<meta charset="utf-8">
<title>7 Tricks every Orchard Keeper Quietly Hides — Cover</title>
<link href="https://fonts.googleapis.com/css2?family=Caveat+Brush&display=swap" rel="stylesheet">
<style>
  :root {
    --backdrop: #d3d3d3;
    --cover-shadow: #383838;
    --cover-white: #ffffff;
    --title-blue: #1ea3dc;
    --board-face: #eeefef;
    --board-frame: #c4c7c8;
    --portrait-tone-a: #f3eeeb;
    --portrait-tone-b: #cdb3a5;
  }
  * { box-sizing: border-box; margin: 0; padding: 0; }
  html, body {
    width: 1200px;
    height: 1000px;
    overflow: hidden;
    background: var(--backdrop);
  }
  .cover {
    position: absolute;
    left: 353px;
    top: 82px;
    width: 550px;
    height: 778px;
    background: var(--cover-white);
    box-shadow: -20px 18px 2px var(--cover-shadow);
    overflow: hidden;
  }
  .cover__board {
    position: absolute;
    left: 34px;
    top: 98px;
    width: 530px;
    height: 400px;
    background: var(--board-face);
    border: 5px solid var(--board-frame);
    border-radius: 3px;
  }
  .cover__portrait {
    position: absolute;
    left: 185px;
    top: 370px;
    width: 365px;
    height: 408px;
    background: radial-gradient(ellipse at 70% 40%, var(--portrait-tone-b) 0%, var(--portrait-tone-a) 60%, var(--cover-white) 100%);
    clip-path: polygon(145px 0, 365px 0, 365px 408px, 0 408px, 0 200px, 145px 110px);
  }
  .cover__title {
    position: absolute;
    left: 68px;
    top: 52px;
    width: 470px;
    font-family: "Caveat Brush", cursive;
    font-weight: 400;
    font-size: 88px;
    line-height: 106px;
    color: var(--title-blue);
    letter-spacing: -1px;
  }
  .cover__title span { display: block; white-space: nowrap; }
  .cover__title .indent { padding-left: 68px; }
</style>
</head>
<body>
  <main class="cover">
    <div class="cover__board" role="img" aria-label="Photo of a whiteboard on an easel stand"></div>
    <div class="cover__portrait" role="img" aria-label="Photo of a doctor in a white coat writing on the whiteboard with a marker"></div>
    <h1 class="cover__title">
      <span>7 Tricks every</span>
      <span>Orchard Keeper</span>
      <span>Quietly</span>
      <span class="indent">Hides</span>
    </h1>
  </main>
</body>
</html>
```